BottleNook Restuarant Postcard

I have a list of restaurant owners that I need to get to take Action on my Website.

The Website is:

http://www.bottlenook.example

The goal of the Post card will be to mail to Restaurant Owners and encourage them to visit our Website and enter some details about their property on our website.

The Card Must Contain the Text:

Get New Customers From:

www.BottleNook.example

admin@bottlenook.example

323-555-0147

The steps I need recipients of the card to take

1. Visit: www.BottleNook.example

2. Find your Restaurant using the Search Box

3. Click on Restaurant

4. Click on “Do You”

5. Enter your Corkage Fee Details!

I have loaded a some files:

I added some Logos, as well as some screenshots of my attempts at the post card.

Industry/Entity Type

Restaurant

```html
<!DOCTYPE html>
<html lang="en">
<head>
<meta charset="utf-8">
<title>BottleNook Restaurant Postcard</title>
<link rel="stylesheet" href="https://fonts.googleapis.com/css2?family=Raleway:wght@300;400;500&display=swap">
<style>
  :root {
    --olive: #a8a437;
    --sage: #6b8f78;
    --paper: #ffffff;
    --ink: #1c1c1c;
    --muted: #8a8a80;
    --backdrop: #e9e6e0;
  }
  * { margin: 0; padding: 0; box-sizing: border-box; }
  html, body {
    width: 1200px; height: 512px; overflow: hidden;
    background: var(--backdrop);
    font-family: "Raleway", sans-serif;
  }
  .canvas { position: relative; width: 1200px; height: 512px; }

  .card {
    position: absolute; background: var(--paper); overflow: hidden;
    box-shadow: 0 2px 6px rgba(0,0,0,0.15);
  }

  /* Front */
  .card--front { left: 36px; top: 43px; width: 551px; height: 426px; }
  .front__headline-band {
    position: absolute; left: 0; top: 10px; width: 100%; height: 123px;
    background: var(--olive);
  }
  .front__headline {
    position: absolute; left: 0; top: 37px; width: 100%;
    text-align: center; color: var(--paper);
    font-weight: 300; font-size: 37px; letter-spacing: 0.5px;
  }
  .brand {
    position: absolute; left: 0; top: 138px; width: 100%; text-align: center;
  }
  .brand__name {
    display: inline-flex; align-items: center; gap: 8px;
    font-weight: 500; font-size: 40px; color: var(--ink); line-height: 1;
  }
  .brand__dot { width: 12px; height: 12px; border-radius: 50%; background: var(--ink); }
  .brand__tagline {
    margin-top: 8px; font-weight: 400; font-size: 16px; color: var(--ink);
  }
  .front__contact-band {
    position: absolute; left: 0; top: 240px; width: 100%; height: 150px;
    background: var(--sage);
  }
  .contact-list { list-style: none; position: absolute; left: 0; top: 8px; }
  .contact-item {
    display: flex; align-items: center; height: 41px;
    color: #e4ece6; font-weight: 300; font-size: 29px;
  }
  .contact-item svg { width: 22px; height: 22px; margin-left: 38px; margin-right: 26px; flex: none; }
  .front__rule {
    position: absolute; left: 0; top: 400px; width: 100%; height: 10px;
    background: var(--olive);
  }

  /* Back */
  .card--back { left: 616px; top: 40px; width: 555px; height: 429px; }
  .back__brand {
    position: absolute; left: 0; top: 16px;
    font-weight: 500; font-size: 33px; color: var(--ink); line-height: 1;
    display: flex; align-items: center; gap: 6px;
  }
  .back__brand .brand__dot { width: 10px; height: 10px; }
  .back__steps-band {
    position: absolute; left: 0; top: 59px; width: 100%; height: 96px;
    background: var(--sage);
  }
  .back__steps-title {
    position: absolute; left: 10px; top: 30px;
    color: #e4ece6; font-weight: 300; font-size: 27px;
  }
  .back__steps-box {
    position: absolute; left: 0; top: 171px; width: 391px; height: 224px;
    background: var(--olive);
  }
  .steps {
    list-style: none; position: absolute; left: 14px; top: 12px;
    color: var(--paper); font-weight: 400; font-size: 23px; line-height: 24px;
  }
  .steps li { margin-bottom: 10px; }
  .steps li.tight { margin-bottom: 2px; }
  .back__divider {
    position: absolute; left: 391px; top: 0; width: 8px; height: 100%;
    background: var(--olive);
  }
  .address {
    position: absolute; left: 405px; top: 285px;
    font-size: 16px; line-height: 20px; font-weight: 400;
  }
  .address__name { color: var(--ink); }
  .address__line { color: var(--muted); font-weight: 300; }
</style>
</head>
<body>
<main class="canvas">

  <section class="card card--front" aria-label="Postcard front">
    <div class="front__headline-band">
      <h1 class="front__headline">Get new customers from:</h1>
    </div>
    <div class="brand">
      <div class="brand__name"><span class="brand__dot"></span>BottleNook</div>
      <p class="brand__tagline">Online Corkage Fee Directory</p>
    </div>
    <div class="front__contact-band">
      <ul class="contact-list">
        <li class="contact-item">
          <svg viewBox="0 0 24 24" fill="#e4ece6" aria-hidden="true"><rect x="2" y="3" width="20" height="13" rx="1"/><rect x="4" y="5" width="16" height="9" fill="#6b8f78"/><rect x="9" y="17" width="6" height="2"/><rect x="6" y="19" width="12" height="2"/></svg>
          www.BottleNook.example
        </li>
        <li class="contact-item">
          <svg viewBox="0 0 24 24" fill="#e4ece6" aria-hidden="true"><rect x="2" y="5" width="20" height="14"/><path d="M2 5 L12 13 L22 5" fill="none" stroke="#6b8f78" stroke-width="2"/></svg>
          admin@bottlenook.example
        </li>
        <li class="contact-item">
          <svg viewBox="0 0 24 24" fill="#e4ece6" aria-hidden="true"><path d="M7 3 L10 3 L11 8 L9 9.5 C10 12 12 14 14.5 15 L16 13 L21 14 L21 17 C21 19 19 21 17 21 C10 20 4 14 3 7 C3 5 5 3 7 3 Z"/></svg>
          323-555-0147
        </li>
      </ul>
    </div>
    <div class="front__rule"></div>
  </section>

  <section class="card card--back" aria-label="Postcard back">
    <div class="back__steps-band">
      <h2 class="back__steps-title">Follow these quick steps:</h2>
    </div>
    <div class="back__brand"><span class="brand__dot"></span>BottleNook</div>
    <div class="back__steps-box">
      <ol class="steps">
        <li>1. Visit: www.BottleNook.example</li>
        <li class="tight">2. Find your Restaurant</li>
        <li>using the Search Box</li>
        <li>3. Click on Restaurant</li>
        <li>4. Click on “Do You”</li>
        <li class="tight">5. Enter your Corkage</li>
        <li>Fee Details!</li>
      </ol>
    </div>
    <div class="back__divider"></div>
    <address class="address" style="font-style: normal;">
      <div class="address__name">Recipient Name</div>
      <div class="address__line">Address Line 1</div>
      <div class="address__line">Address Line 2</div>
      <div class="address__line">Address Line 3</div>
      <div class="address__line">Address Line 4</div>
    </address>
  </section>

</main>
</body>
</html>
```